Pool Website

Need a simple front page and one internal page for a pool construction website. Please read the Must Have section for info. We uploaded 2 logos, one with color and one black and white. The colors you use in the logo can be changed, we used Century Gothic for the typing under the logo.

Nice clean design. The main back behind the site can be any color but we want the content back ground to be white.

We want a scrolling photo gallery (it doesn't have to scroll in your sample just know that's what we are envisioning) on the front page and the menu, and maybe a couple of photos down below to be clicked on such as this http://www.delmarwaterworks.example/

The 2ndary page would still have a header and menu and some type of cool design. Could be similar to this http://www.delmarwaterworks.example/about-us/awards.html

Also some other designs they like are here http://www.tessaloop.example/14-examples-of-clean-modern-website-design-inspiration/ I realize not all of these could have a image scroller on the front page which is fine.

Please do not copy their site exactly though it must be different.

For now you can just use sample stock photography for your photos for the design but ultimately we will swap them out for our own photos so there will not be a need to purchase stock photography of pools.

Menus will include Home - About - Services - Gallery - Contact - Blog

The current site is http://www.hughwestmorepools.example/ we do not want it to look anything like this. It's way too dark and just not professional looking. We want this new site to look very slick and professional.

We also want a space for social networking logos etc.

I have also attached 2 zip files that contain photos that may be used in the design. You do not have to use them all but you are welcome to use a few. Most will be put in the photo gallery.

Colors: Blues, white, grays, black, etc.
Updates

Added several photos that can be used in the design. Obviously you do not have to use them all most will be in the photo gallery but you're welcome to use some for your design. 

Target Market(s)

People with money for residential pools or companies that want corporate pools. Are target location is Miami and California

Industry/Entity Type

Construction

Font styles to use
Serif
Sans Serif

Requirements
Must have
• Nice clean design. The main back behind the site can be any color but we want the content back ground to be white.

```html
<!DOCTYPE html>
<html lang="en">
<head>
<meta charset="utf-8">
<title>Hugh Westmore Pools</title>
<link rel="stylesheet" href="https://fonts.googleapis.com/css2?family=Questrial&family=Arimo:wght@400;700&display=swap">
<style>
:root{
  --header-blue:#003594;
  --navy:#0e1f73;
  --ink:#10237a;
  --cyan:#2ac4d6;
  --white:#ffffff;
  --text:#222;
  --band-grey:#e6e6e6;
  --tile-blue:#5a9be8;
}
*{margin:0;padding:0;box-sizing:border-box}
html,body{width:1043px;height:1200px;overflow:hidden;background:var(--white)}
body{position:relative;font-family:"Arimo",Arial,sans-serif;color:var(--text)}
.site-header{position:absolute;left:0;top:0;width:1043px;height:217px;background:var(--header-blue)}
.brand{position:absolute;left:0;width:1043px;top:52px;text-align:center}
.brand-mark{display:inline-block;width:18px;height:18px;background:var(--cyan);vertical-align:middle;margin-right:10px}
.brand-name{font-family:"Questrial",sans-serif;font-size:30px;color:var(--white);vertical-align:middle;letter-spacing:1px}
.tagline-rule{position:absolute;top:156px;height:1px;background:var(--cyan)}
.tagline{position:absolute;top:146px;left:0;width:1043px;text-align:center;font-family:"Questrial",sans-serif;font-size:14px;color:var(--cyan)}
.tagline span{background:var(--header-blue);padding:0 12px}
.main-nav a,.footer-nav a{position:absolute;font-family:"Questrial",sans-serif;color:var(--white);text-decoration:none;transform:translateX(-50%);white-space:nowrap}
.main-nav a{top:181px;font-size:15px}
.social{position:absolute;width:21px;height:21px;border-radius:4px;background:var(--white)}
.hero{position:absolute;left:0;top:217px;width:1043px;height:239px}
.hero-side{position:absolute;top:0;width:130px;height:130px;background:linear-gradient(to bottom,var(--tile-blue),#bcd7f7 70%,var(--white))}
.hero-slide{position:absolute;left:130px;top:0;width:782px;height:239px;border:2px solid var(--ink);border-top:none;border-radius:0 0 14px 14px;overflow:hidden;background:linear-gradient(100deg,#b9a87f 0%,#4f4a38 30%,#1a2420 60%,#1f5a5c 100%)}
.hero-arrow{position:absolute;top:100px}
.hero-dots{position:absolute;left:356px;bottom:4px;width:72px;height:14px;border-radius:7px;background:rgba(0,0,0,.45);display:flex;justify-content:space-evenly;align-items:center}
.hero-dots i{width:7px;height:7px;border-radius:50%;border:1px solid var(--white)}
.hero-dots i.on{background:var(--white)}
.welcome{position:absolute;left:0;width:1043px;text-align:center}
.welcome-line{top:488px;font-size:19px;color:#333}
.welcome-line b{color:var(--ink)}
.welcome-sub{top:513px;font-size:22px;font-weight:700;color:var(--ink)}
.welcome-area{top:551px;font-size:15px;color:#222}
.feature{position:absolute;top:591px;width:252px;height:215px;border:2px solid var(--ink);border-radius:12px;overflow:hidden;background:var(--navy)}
.feature-photo{height:141px}
.feature-caption{height:72px;display:flex;flex-direction:column;justify-content:center;align-items:center;text-align:center;font-size:15.5px;line-height:18px;color:var(--cyan)}
.feature-caption b{color:var(--white)}
.showroom-band{position:absolute;left:0;top:845px;width:1043px;height:198px;background:var(--band-grey);border-top:3px solid #d9d9d9}
.showroom{position:absolute;left:177px;top:50px;font-size:16px;line-height:21px;color:var(--ink)}
.showroom h2{font-size:17.5px;font-weight:700}
.showroom-phone{display:flex;align-items:center;margin-top:3px;margin-left:-25px;font-size:24px;font-weight:700}
.showroom-phone svg{margin-right:8px}
.map{position:absolute;left:393px;top:0;width:650px;height:195px;background:linear-gradient(135deg,#eceae3,#e3e0d6)}
.map-pin{position:absolute;left:287px;top:80px}
.site-footer{position:absolute;left:0;top:1043px;width:1043px;height:157px;background:var(--navy);color:var(--white)}
.service-links{position:absolute;top:30px;left:0;width:1043px;text-align:center;font-size:12.5px;white-space:nowrap}
.service-links span{margin:0 8px}
.footer-rule{position:absolute;left:133px;top:67px;width:779px;height:1px;background:#2b3c8f}
.footer-nav a{top:103px;font-size:15px}
.footer-social{position:absolute;top:95px;width:28px;height:28px;border-radius:5px;background:var(--white)}
.footer-contact{position:absolute;left:623px;top:84px;width:320px;text-align:center;white-space:nowrap}
.footer-contact h3{font-weight:400;font-size:16px;line-height:20px}
.footer-contact p{font-size:12.5px;line-height:17px}
.footer-contact strong{font-size:15px}
</style>
</head>
<body>
<header class="site-header">
  <div class="brand"><span class="brand-mark"></span><span class="brand-name">Hugh Westmore Pools</span></div>
  <div class="tagline-rule" style="left:133px;width:780px"></div>
  <div class="tagline"><span>Family Owned for Over 30 Years!</span></div>
  <nav class="main-nav">
    <a href="#" style="left:222px">Home</a>
    <a href="#" style="left:318px">About</a>
    <a href="#" style="left:420px">Services</a>
    <a href="#" style="left:521px">Gallery</a>
    <a href="#" style="left:630px">Contact</a>
    <a href="#" style="left:729px">Blog</a>
  </nav>
  <span class="social" style="left:813px;top:178px"></span>
  <span class="social" style="left:850px;top:178px"></span>
</header>

<section class="hero">
  <div class="hero-side" style="left:0"></div>
  <div class="hero-side" style="left:913px"></div>
  <div class="hero-slide" role="img" aria-label="Slideshow photo of a lit pool behind a columned villa at night">
    <svg class="hero-arrow" style="left:16px" width="20" height="64" viewBox="0 0 20 64"><polyline points="18,2 2,32 18,62" fill="none" stroke="#fff" stroke-width="1.5"/></svg>
    <svg class="hero-arrow" style="right:16px" width="20" height="64" viewBox="0 0 20 64"><polyline points="2,2 18,32 2,62" fill="none" stroke="#fff" stroke-width="1.5"/></svg>
    <div class="hero-dots"><i class="on"></i><i></i><i></i><i></i><i></i></div>
  </div>
</section>

<p class="welcome welcome-line"><b>Welcome</b> to Hugh Westmore Pool Contracting, Inc.</p>
<p class="welcome welcome-sub">Your Ultimate Dealer!</p>
<p class="welcome welcome-area">Serving Broward, Palm &amp;Miami-Dade Counties</p>

<article class="feature" style="left:129px">
  <div class="feature-photo" role="img" aria-label="Photo of a blue pool with a stone waterfall" style="background:linear-gradient(to bottom,#3e5a34,#6f8fa8 45%,#2c6fc0)"></div>
  <div class="feature-caption"><span>Full Service</span><b>Pool Company</b></div>
</article>
<article class="feature" style="left:395px">
  <div class="feature-photo" role="img" aria-label="Photo of a lit pool beside a covered patio at dusk" style="background:linear-gradient(to bottom,#5a4a36,#3a3a2e 50%,#2a7f9a)"></div>
  <div class="feature-caption"><b>Residential <span style="color:var(--cyan);font-weight:400">and</span></b><b>Commercial Pools</b><span>in South Florida</span></div>
</article>
<article class="feature" style="left:660px">
  <div class="feature-photo" role="img" aria-label="Photo of a freeform pool with a fire bowl" style="background:linear-gradient(to bottom,#8c9a7a,#7d8c96 40%,#3c6f86)"></div>
  <div class="feature-caption"><span>Maintenance,</span><b>Repairs and Renovations</b></div>
</article>

<section class="showroom-band">
  <div class="showroom">
    <h2>Visit our showroom</h2>
    <p>2140 NW 41 Court,<br>Coral Harbor,<br>Florida 33099</p>
    <div class="showroom-phone">
      <svg width="17" height="20" viewBox="0 0 24 24"><path fill="#10237a" d="M6.6 10.8c1.4 2.8 3.8 5.1 6.6 6.6l2.2-2.2c.3-.3.7-.4 1-.2 1.1.4 2.3.6 3.6.6.6 0 1 .4 1 1V20c0 .6-.4 1-1 1C10.6 21 3 13.4 3 4c0-.6.4-1 1-1h3.5c.6 0 1 .4 1 1 0 1.3.2 2.5.6 3.6.1.3 0 .7-.2 1z"/></svg>
      954-555-0148
    </div>
  </div>
  <div class="map" role="img" aria-label="Street map showing the showroom location">
    <svg class="map-pin" width="30" height="42" viewBox="0 0 30 42"><path d="M15 0C6.7 0 0 6.7 0 15c0 11 15 27 15 27s15-16 15-27C30 6.7 23.3 0 15 0z" fill="#10237a"/><circle cx="15" cy="15" r="5.5" fill="#fff"/></svg>
  </div>
</section>

<footer class="site-footer">
  <p class="service-links">Commercial Pool Installation<span>I</span>Pool Maintenance<span>I</span>Pool Remodeling<span>I</span>Pool Renovation<span>I</span>Swimming Pool Installation<span>I</span>Pool Repair</p>
  <div class="footer-rule"></div>
  <nav class="footer-nav">
    <a href="#" style="left:163px">Home</a>
    <a href="#" style="left:224px">About</a>
    <a href="#" style="left:290px">Services</a>
    <a href="#" style="left:357px">Gallery</a>
    <a href="#" style="left:432px">Contact</a>
    <a href="#" style="left:496px">Blog</a>
  </nav>
  <span class="footer-social" style="left:531px"></span>
  <span class="footer-social" style="left:569px"></span>
  <div class="footer-contact">
    <h3>Hugh Westmore Pools</h3>
    <p>Serving Broward and Palm Beach Counties</p>
    <p>Call Us Now <strong>954-555-0148</strong></p>
  </div>
</footer>
</body>
</html>
```